Korvane Design Template

I'd like to have a powerpoint templates. In particular a resume template design upon the Korvane website (www.korvane.nl). Korvane is the overarching label in grey tones. The website is therefore more focussed on Techkorvane in blue colors, I expect more korvanes in the future with different color tones.

The resume template can hopefulle reused as template for business development and more.

The template should be highly professional. Preferably with a one-pager summary in front and 2 work experience details and last page with education/certificates and competences.

The onepager master slide should include
- Profile picture
- Name
- About me (optionally to mention this literally, this text can be alongside/next to the profile picture
- Table of work experience summary

In short, age, place of living, mobile phone nr in footer?
In the workexperience it describes Role, timeframe, subtitle used in slide 1 (summary of role), with a section of scope and section for achievements.

From a visual perspective, please stick to the logos provided. You may want to grey out the logo. Keep the logo as it is and work with collor pallet
Light Grey: #DEDEDE
Medium Grey: #888888
Black: #3A3A3A

```html
<!DOCTYPE html>
<html lang="en">
<head>
<meta charset="utf-8">
<title>Korvane Resume Presentation Template</title>
<link rel="stylesheet" href="https://fonts.googleapis.com/css2?family=Inter:wght@300;400;500;600&family=Poppins:wght@400;500;600;700&display=swap">
<style>
  :root {
    --board: #888888;
    --light: #DEDEDE;
    --panel-light: #D4D4D4;
    --dark: #3A3A3A;
    --dark-2: #363636;
    --mid: #888888;
    --line-dark: #9A9A9A;
    --line-light: #5A5A5A;
    --text-soft: #BDBDBD;
    --photo-a: #9C9C9C;
    --photo-b: #5E5E5E;
  }
  * { margin: 0; padding: 0; box-sizing: border-box; }
  html, body { width: 860px; height: 1200px; overflow: hidden; background: var(--board); }
  body { position: relative; font-family: "Inter", sans-serif; }

  .slide { position: absolute; width: 379px; height: 213px; overflow: hidden; }
  .slide > * { position: absolute; }
  .col-left { left: 53px; }
  .col-right { left: 446px; }
  .row-1 { top: 36px; } .row-2 { top: 261px; } .row-3 { top: 486px; } .row-4 { top: 711px; } .row-5 { top: 936px; }
  .is-dark { background: var(--dark); color: var(--light); }
  .is-light { background: var(--panel-light); color: var(--dark); }

  .brand { left: 39px; top: 20px; font-family: "Inter", sans-serif; font-weight: 500; font-size: 10px; letter-spacing: 0.1px; color: var(--dark); }
  .is-dark .brand { color: var(--light); }
  .eyebrow { left: 163px; top: 17px; font-size: 4.3px; letter-spacing: 0.1px; text-decoration: underline; color: var(--dark); }
  .is-dark .eyebrow { color: var(--light); }
  .eyebrow b { font-weight: 600; }

  .rule-h { height: 0; border-top: 0.6px solid var(--line-light); }
  .is-dark .rule-h { border-color: var(--line-dark); }
  .rule-v { width: 0; border-left: 0.6px solid var(--line-light); }
  .rule-v.dashed { border-left-style: dashed; border-color: var(--line-dark); }

  .foot { top: 195px; font-size: 4.3px; color: #6A6A6A; }
  .is-dark .foot { color: var(--text-soft); }
  .foot-left { left: 30px; }
  .foot-num { left: 183px; width: 12px; text-align: center; }
  .foot-right { right: 30px; }

  .heading { font-weight: 300; font-size: 16px; line-height: 19px; letter-spacing: 0.2px; }
  .tiny { font-size: 4.5px; line-height: 9.3px; }
  .badge { width: 17.5px; height: 6.3px; border-radius: 1px; font-size: 3.8px; line-height: 6.3px; text-align: right; padding-right: 3px; }
  .ring { width: 20px; height: 20px; border: 0.6px solid var(--line-light); border-radius: 50%; }
  .is-dark .ring { border-color: var(--line-dark); }
  .photo { background: linear-gradient(160deg, var(--photo-a), var(--photo-b)); }

  /* Slide 1 — profile summary */
  .profile-card { left: 13px; top: 13px; width: 210px; height: 187px; background: var(--light); }
  .profile-card .brand { left: 26px; top: 6px; }
  .pill { left: 96px; top: 25.5px; width: 105px; height: 7.4px; border: 0.6px solid var(--dark); border-radius: 1.5px; font-family: "Poppins", sans-serif; font-size: 3.8px; line-height: 6.4px; padding-left: 5px; color: var(--dark); }
  .name-first { left: 40px; top: 46px; font-family: "Poppins", sans-serif; font-weight: 700; font-size: 24px; color: var(--dark); }
  .name-last { left: 40px; top: 72px; font-family: "Poppins", sans-serif; font-size: 18px; letter-spacing: 2px; color: var(--dark); }
  .summary-title { left: 40px; top: 107px; font-family: "Poppins", sans-serif; font-weight: 600; font-size: 6.6px; letter-spacing: 0.2px; color: var(--dark); }
  .summary-role { left: 40px; top: 120px; font-family: "Poppins", sans-serif; font-size: 4.8px; color: var(--dark); }
  .summary-years { left: 167px; top: 120px; width: 30px; text-align: right; font-family: "Poppins", sans-serif; font-size: 4.8px; color: var(--dark); }
  .summary-text { left: 40px; top: 138px; width: 157px; font-family: "Poppins", sans-serif; font-size: 3.7px; line-height: 5.7px; text-align: justify; color: var(--dark); }
  .profile-photo { left: 253px; top: 21px; width: 77px; height: 77px; border-radius: 50%; border: 1px solid var(--mid); }
  .about-title { left: 246px; top: 110px; font-family: "Poppins", sans-serif; font-size: 5px; }
  .about-text { left: 246px; top: 118px; width: 94px; font-family: "Poppins", sans-serif; font-size: 3.7px; line-height: 5.7px; text-align: justify; }
  .contact { left: 289px; top: 185px; font-family: "Poppins", sans-serif; font-size: 4.4px; color: var(--text-soft); }

  /* Work experience timeline */
  .date-bar { left: 104px; width: 55px; height: 6.3px; background: var(--dark); color: var(--light); font-size: 4.3px; line-height: 6.3px; text-align: right; padding-right: 2px; border-radius: 1px; }
  .role-title { left: 169px; font-size: 4.6px; font-weight: 600; text-decoration: underline; }
  .role-text { left: 169px; width: 175px; font-size: 4.4px; line-height: 9.4px; }

  /* Scope / achievements */
  .split-panel { left: 171px; top: 45.5px; width: 208px; height: 168px; background: var(--dark); }
  .tag { left: 38.6px; top: 80px; width: 77px; height: 12.7px; background: var(--dark); color: var(--light); font-weight: 600; font-size: 6px; line-height: 12.7px; padding-left: 7px; }
  .tag small { font-size: 4px; margin-right: 1px; }
  .point-badge { left: 206px; background: var(--light); color: var(--dark); }
  .point-text { left: 231px; width: 132px; color: var(--light); }
  .panel-foot { right: 30px; top: 195px; font-size: 4.3px; font-weight: 600; color: var(--light); }

  /* Certificates */
  .cert-block { left: 0; top: 42px; width: 154.5px; height: 144px; background: var(--dark); }
  .cert-item { left: 237px; font-size: 6px; }
  .cert-badge { left: 212px; border: 0.6px solid var(--dark); color: var(--dark); }

  /* Reviews */
  .review-panel { left: 0; top: 28.5px; width: 115px; height: 156px; background: var(--dark); }
  .review-strip { left: 361px; top: 28.5px; width: 18px; height: 156px; background: var(--dark); }
  .quote-mark { left: 141px; top: 53px; font-family: "Poppins", sans-serif; font-weight: 700; font-size: 28px; line-height: 28px; }
  .reviewer { left: 165px; font-size: 5.8px; }
  .review-text { left: 228px; width: 118px; font-size: 4.6px; line-height: 9.4px; color: #555; }
</style>
</head>
<body>

<!-- 1 · Profile summary -->
<section class="slide is-dark col-left row-1">
  <div class="profile-card"></div>
  <div class="rule-v dashed" style="left:29px; top:13px; height:187px;"></div>
  <div class="brand" style="top:20px;">Techkorvane</div>
  <div class="pill">Resume Presentation</div>
  <div class="name-first">Daan</div>
  <div class="name-last">Verhoeven</div>
  <div class="summary-title">WORK EXPERIENCE</div>
  <div class="rule-h" style="left:114px; top:111px; width:91px; border-color:var(--dark);"></div>
  <div class="summary-role">Korvane Lead</div>
  <div class="summary-years">2019 – 2025</div>
  <p class="summary-text">Lorem ipsum dolor sit amet, consectetur adipiscing elit. Nullam pharetra in lorem at laoreet. Donec hendrerit libero eget est tempor, quis tempus arcu elementum. In elementum elit at dui tristique feugiat. Mauris convallis, mi at mattis malesuada, neque nulla volutpat.</p>
  <div class="ring" style="left:39px; top:170px; border-color:var(--dark);"></div>
  <svg style="left:49px; top:178px;" width="162" height="6" viewBox="0 0 162 6"><line x1="0" y1="3" x2="158" y2="3" stroke="#3A3A3A" stroke-width="0.6"/><path d="M155 1 L160 3 L155 5 Z" fill="#3A3A3A"/></svg>
  <div class="profile-photo photo" role="img" aria-label="Profile photo of the candidate"></div>
  <div class="about-title">About me</div>
  <p class="about-text">Lorem ipsum dolor sit amet, consectetur adipiscing elit. Nullam pharetra in lorem at laoreet. Donec hendrerit libero eget est tempor, quis tempus arcu elementum. In elementum elit at dui tristique feugiat. Mauris convallis, mi at mattis malesuada, neque nulla volutpat.</p>
  <div class="contact">daan.verhoeven@korvane.nl</div>
</section>

<!-- 2 · Work experience timeline -->
<section class="slide is-light col-right row-1">
  <div class="brand">Techkorvane</div>
  <div class="eyebrow"><b>RESUME</b> PRESENTATION</div>
  <h2 class="heading" style="left:166px; top:45px;">WORK<br>EXPERIENCE</h2>
  <div class="rule-h" style="left:0; top:86.5px; width:379px;"></div>
  <div class="rule-v" style="left:93px; top:86.5px; height:105.5px;"></div>
  <div class="date-bar" style="top:97px;">2018 - 2019</div>
  <div class="role-title" style="top:97px;">Title of Role here</div>
  <p class="role-text" style="top:106px;">In the workexperience it describes Role, timeframe, subtitle used in slide 1 (summary of role), with a section of scope and section for achievements.</p>
  <div class="date-bar" style="top:145.5px;">2020 - 2022</div>
  <div class="role-title" style="top:145.5px;">Title of Role here</div>
  <p class="role-text" style="top:154.5px;">In the workexperience it describes Role, timeframe, subtitle used in slide 1 (summary of role), with a section of scope and section for achievements.</p>
  <div class="rule-h" style="left:0; top:192px; width:379px;"></div>
  <div class="foot foot-left">Korvane Lead</div>
  <div class="foot foot-num">06</div>
  <div class="foot foot-right">Daan Verhoeven</div>
</section>

<!-- 3 · Scope -->
<section class="slide is-light col-left row-2">
  <div class="split-panel"></div>
  <div class="brand">Techkorvane</div>
  <div class="eyebrow"><b>RESUME</b> PRESENTATION</div>
  <div class="ring" style="left:18px; top:50px;"></div>
  <div class="rule-h" style="left:28px; top:60px; width:143px;"></div>
  <div class="tag"><small>SEC2</small> scope</div>
  <h2 class="heading" style="left:38px; top:105px;">WORK<br>EXPERIENCE</h2>
  <div class="badge point-badge" style="top:78px;">01</div>
  <p class="tiny point-text" style="top:76px;">About me (optionally to mention this literally, this text can be alongside/next to the profile picture</p>
  <div class="badge point-badge" style="top:100.7px;">02</div>
  <p class="tiny point-text" style="top:98.7px;">About me (optionally to mention this literally, this text can be alongside/next to the profile picture</p>
  <div class="badge point-badge" style="top:123.4px;">03</div>
  <p class="tiny point-text" style="top:121.4px;">About me (optionally to mention this literally, this text can be alongside/next to the profile picture</p>
  <div class="rule-h" style="left:0; top:192px; width:379px;"></div>
  <div class="foot foot-left">Korvane Lead</div>
  <div class="panel-foot">Daan Verhoeven</div>
</section>

<!-- 4 · Achievements -->
<section class="slide is-light col-right row-2">
  <div class="split-panel"></div>
  <div class="brand">Techkorvane</div>
  <div class="eyebrow"><b>RESUME</b> PRESENTATION</div>
  <div class="ring" style="left:18px; top:50px;"></div>
  <div class="rule-h" style="left:28px; top:60px; width:143px;"></div>
  <div class="tag"><small>SEC2</small> achievements</div>
  <h2 class="heading" style="left:38px; top:105px;">WORK<br>EXPERIENCE</h2>
  <div class="badge point-badge" style="top:78px;">01</div>
  <p class="tiny point-text" style="top:76px;">About me (optionally to mention this literally, this text can be alongside/next to the profile picture</p>
  <div class="badge point-badge" style="top:100.7px;">02</div>
  <p class="tiny point-text" style="top:98.7px;">About me (optionally to mention this literally, this text can be alongside/next to the profile picture</p>
  <div class="badge point-badge" style="top:123.4px;">03</div>
  <p class="tiny point-text" style="top:121.4px;">About me (optionally to mention this literally, this text can be alongside/next to the profile picture</p>
  <div class="rule-h" style="left:0; top:192px; width:379px;"></div>
  <div class="foot foot-left">Korvane Lead</div>
  <div class="panel-foot">Daan Verhoeven</div>
</section>

<!-- 5 · Education -->
<section class="slide is-dark col-left row-3">
  <div class="brand">Techkorvane</div>
  <div class="eyebrow"><b>RESUME</b> PRESENTATION</div>
  <div class="rule-v dashed" style="left:225px; top:0; height:192px;"></div>
  <h2 class="heading" style="left:37px; top:71px; font-size:15px;">EDUCATION</h2>
  <p style="left:37px; top:98px; width:120px; font-size:4.8px; line-height:9.4px; letter-spacing:0.1px; color:var(--text-soft);">In the workexperience it describes Role, timeframe, subtitle used in slide 1 (summary of role), with a section of scope and section for achievements.</p>
  <div style="left:286px; top:25px; font-size:4.8px; color:var(--text-soft);">2010- 2013</div>
  <div class="photo" style="left:253px; top:42px; width:97px; height:118px; background:linear-gradient(170deg,#7C7C7C,#2E2E2E);" role="img" aria-label="Graduation photo in gown and cap holding a blank board"></div>
  <div class="rule-h" style="left:0; top:192px; width:379px;"></div>
  <div class="foot foot-left">Korvane Lead</div>
  <div class="foot foot-num">05</div>
  <div class="foot foot-right">Daan Verhoeven</div>
</section>

<!-- 6 · Certificates -->
<section class="slide is-light col-right row-3">
  <div class="brand">Techkorvane</div>
  <div class="eyebrow"><b>RESUME</b> PRESENTATION</div>
  <div class="cert-block"></div>
  <div class="rule-h" style="left:0; top:57px; width:154.5px; border-color:var(--line-dark);"></div>
  <div class="photo" style="left:19.6px; top:78px; width:112px; height:79px; background:linear-gradient(160deg,#D8D8D8,#A8A8A8);" role="img" aria-label="Certificate of achievement document"></div>
  <div class="ring" style="left:163px; top:54.5px;"></div>
  <svg style="left:173px; top:61.5px;" width="34" height="6" viewBox="0 0 34 6"><line x1="0" y1="3" x2="30" y2="3" stroke="#3A3A3A" stroke-width="0.6"/><path d="M28 1 L33 3 L28 5 Z" fill="#3A3A3A"/></svg>
  <h2 class="heading" style="left:212px; top:54px; font-size:15.5px;">CERTIFICATES</h2>
  <div class="badge cert-badge" style="top:90px;">01</div>
  <div class="cert-item" style="top:89.5px;">Certified One Title here</div>
  <div class="badge cert-badge" style="top:103.5px;">02</div>
  <div class="cert-item" style="top:103px;">Certified Two Title here</div>
  <div class="rule-h" style="left:0; top:192px; width:379px;"></div>
  <div class="foot foot-left">Korvane Lead</div>
  <div class="foot foot-num">09</div>
  <div class="foot foot-right">Daan Verhoeven</div>
</section>

<!-- 7 · Portfolio -->
<section class="slide is-dark col-left row-4">
  <div class="brand">Techkorvane</div>
  <div class="eyebrow"><b>RESUME</b> PRESENTATION</div>
  <div class="rule-v dashed" style="left:154px; top:0; height:192px;"></div>
  <h2 class="heading" style="left:25px; top:55px; font-size:19.5px; line-height:22px;">PORTFOLIO</h2>
  <div class="photo" style="left:30px; top:109px; width:114px; height:56px; background:linear-gradient(120deg,#9A9A9A,#5A5A5A);" role="img" aria-label="Portfolio image: DevOps concept"></div>
  <div class="photo" style="left:165px; top:58px; width:74px; height:108px; background:linear-gradient(180deg,#8E8E8E,#C4C4C4);" role="img" aria-label="Portfolio image: server room corridor"></div>
  <div class="photo" style="left:242px; top:58px; width:59px; height:72.5px; background:linear-gradient(150deg,#6A6A6A,#3E3E3E);" role="img" aria-label="Portfolio image: digital security concept"></div>
  <div style="left:243px; top:137px; font-size:4.6px; color:var(--light);">www.korvane.nl</div>
  <div class="ring" style="left:242px; top:147px;"></div>
  <svg style="left:252px; top:154px;" width="100" height="6" viewBox="0 0 100 6"><line x1="0" y1="3" x2="96" y2="3" stroke="#BDBDBD" stroke-width="0.6"/><path d="M94 1 L99 3 L94 5 Z" fill="#BDBDBD"/></svg>
  <div class="rule-h" style="left:0; top:192px; width:379px;"></div>
  <div class="foot foot-left">Korvane Lead</div>
  <div class="foot foot-num">12</div>
  <div class="foot foot-right">Daan Verhoeven</div>
</section>

<!-- 8 · Client reviews -->
<section class="slide col-right row-4" style="background:var(--panel-light); color:var(--dark);">
  <div class="eyebrow"><b>RESUME</b> PRESENTATION</div>
  <div class="rule-h" style="left:0; top:28.5px; width:379px;"></div>
  <div style="left:115px; top:28.5px; width:246px; height:156px; background:var(--light);"></div>
  <div class="review-panel"></div>
  <div class="review-strip"></div>
  <div class="rule-h" style="left:0; top:125px; width:115px; border-color:var(--line-dark);"></div>
  <h2 class="heading" style="left:30px; top:63px; font-size:15px; line-height:19px; color:var(--light);">REVIEW<br>FROM<br>CLIENTS</h2>
  <div class="quote-mark">&ldquo;</div>
  <div class="reviewer" style="top:66px;">MILO HARTLEY</div>
  <p class="review-text" style="top:64.5px;">The template should be highly professional. Preferably with a one-pager summary in front and 2 work experience</p>
  <div class="reviewer" style="top:103px;">RUBEN CASTELL</div>
  <p class="review-text" style="top:102px;">The template should be highly professional. Preferably with a one-pager summary in front and 2 work experience</p>
  <div class="reviewer" style="top:137px;">INES MORAVEC</div>
  <p class="review-text" style="top:136px;">The template should be highly professional. Preferably with a one-pager summary in front and 2 work experience</p>
  <div class="rule-h" style="left:0; top:192px; width:379px;"></div>
  <div class="foot foot-left">Korvane Lead</div>
  <div class="foot foot-num">13</div>
  <div class="foot foot-right">Daan Verhoeven</div>
</section>

<!-- 9 · Closing -->
<section class="slide is-dark col-left row-5">
  <div style="left:0; top:58px; width:379px; text-align:center; font-size:22px; font-weight:500; color:var(--light);">Korvane</div>
  <h2 style="left:0; top:129px; width:379px; text-align:center; font-weight:400; font-size:25px; letter-spacing:0.5px; color:var(--light);">THANK YOU!</h2>
  <div style="left:0; top:182px; width:367px; text-align:center; font-size:4.6px; color:var(--text-soft);">@korvane.nl</div>
</section>

</body>
</html>
```